Zielgruppe
Wir verkaufen spezielle Teemischungen an Frauen, die schwanger werden möchten und sich gezielt ein Mädchen oder einen Jungen wünschen. Die Rezeptur unseres Tees, ist speziell auf den jeweiligen Wunsch abgestimmt. Wir verkaufen daher einen Sonnenwiese Tee und einen Sonnenwiese Tee.
Aufgabenstellung
Wir benötigen ein Etikett Design für den Sonnenwiese Tee. Wenn das Etikett fertig designed wurde, würden wir gerne anschließend ein Etikett für den Sonnenwiese Tee designen lassen. Das Design sollte klar, hochwertig und modern wirken. Es sollte erkennbar sein, dass der Tee speziell für Frauen mit einem Mädchenwunsch ist. Die Hintergrundfarbe des Designes bzw. des Etiketts sollte in zart rosa sein.

```html
<!DOCTYPE html>
<html lang="de">
<head>
<meta charset="utf-8">
<title>Sonnenwiese Tee – Etikett</title>
<link rel="stylesheet" href="https://fonts.googleapis.com/css2?family=Barlow+Semi+Condensed:wght@400;500&family=Sacramento&display=swap">
<style>
  :root {
    --page-bg: #f7f0f1;
    --label-top: #f4d3da;
    --label-bottom: #e4b3bf;
    --ink: #ffffff;
    --ink-soft: rgba(255, 255, 255, 0.9);
    --art-a: #f9e4e9;
    --art-b: #ebc3cd;
  }
  * { box-sizing: border-box; margin: 0; padding: 0; }
  html, body {
    width: 1200px;
    height: 1200px;
    overflow: hidden;
    background: var(--page-bg);
  }
  .canvas {
    width: 1200px;
    height: 1200px;
    display: flex;
    align-items: center;
    justify-content: center;
  }
  .label {
    width: 660px;
    height: 900px;
    border-radius: 50% / 38%;
    background: linear-gradient(160deg, var(--label-top) 0%, var(--label-bottom) 100%);
    display: flex;
    flex-direction: column;
    align-items: center;
    padding-top: 120px;
    color: var(--ink);
    font-family: "Barlow Semi Condensed", sans-serif;
  }
  .brand {
    display: flex;
    align-items: center;
    gap: 14px;
    font-weight: 400;
    font-size: 46px;
    letter-spacing: 4px;
    color: var(--ink);
  }
  .brand-dot {
    width: 22px;
    height: 22px;
    border-radius: 50%;
    background: var(--ink);
  }
  .hero-art {
    margin-top: 48px;
    width: 560px;
    height: 240px;
    border-radius: 24px;
    background: radial-gradient(ellipse at center, var(--art-a) 0%, var(--art-b) 80%);
  }
  .product-name {
    margin-top: 28px;
    font-family: "Sacramento", cursive;
    font-weight: 400;
    font-size: 86px;
    line-height: 1;
    white-space: nowrap;
    color: var(--ink);
  }
  .tagline {
    margin-top: 22px;
    text-align: center;
    font-weight: 500;
    font-size: 20px;
    letter-spacing: 1.6px;
    line-height: 1.25;
    text-transform: uppercase;
    color: var(--ink-soft);
  }
  .claim {
    margin-top: 40px;
    display: flex;
    align-items: center;
    gap: 26px;
    font-family: "Sacramento", cursive;
    font-size: 34px;
    color: var(--ink-soft);
  }
  .claim-mark {
    width: 58px;
    height: 58px;
    border-radius: 50%;
    border: 3px solid var(--ink);
  }
  .weight {
    margin-top: 14px;
    font-weight: 500;
    font-size: 26px;
    letter-spacing: 2px;
    color: var(--ink);
  }
</style>
</head>
<body>
<main class="canvas">
  <section class="label">
    <div class="brand"><span class="brand-dot"></span>Duohain</div>
    <div class="hero-art" role="img" aria-label="Illustration eines kleinen Engels mit Heiligenschein zwischen zwei Teezweigen mit Blättern"></div>
    <h1 class="product-name">Sonnenwiese Tee</h1>
    <p class="tagline">Außergewöhnliche Kinderwunsch Rezeptur<br>von Müttern empfohlen</p>
    <div class="claim">
      <span>natürlich</span>
      <span class="claim-mark"></span>
      <span>beeinflussen</span>
    </div>
    <p class="weight">75 GRAMM</p>
  </section>
</main>
</body>
</html>
```